Wageline Associates Business Card Design

We need a business card designed around our new logo. The business card should be modern in design & should communicate success, confidence, power, sophistication. The target market is young business professionals. This is for a human resource & payroll outsourcing business.

```html
<!DOCTYPE html>
<html lang="en">
<head>
<meta charset="utf-8">
<title>Wageline Associates Business Card</title>
<link href="https://fonts.googleapis.com/css2?family=Tinos:wght@400;700&display=swap" rel="stylesheet">
<style>
  :root {
    --stage: #3b4046;
    --card-black: #0d0d0d;
    --card-white: #ffffff;
    --brand-red: #e81f25;
    --deep-red: #a8151a;
    --ink: #1a1a1a;
    --silver: #9a9a9a;
    --divider: #555555;
  }
  * { margin: 0; padding: 0; box-sizing: border-box; }
  html, body { width: 1200px; height: 1000px; overflow: hidden; }
  body {
    background: var(--stage);
    font-family: "Tinos", "Times New Roman", serif;
    position: relative;
  }
  .card {
    position: absolute;
    left: 250px;
    width: 700px;
    height: 400px;
    border-radius: 20px;
    overflow: hidden;
  }
  .card-back { top: 60px; background: var(--card-black); }
  .card-front { top: 540px; background: var(--card-white); }
  .card-art { position: absolute; inset: 0; }
  .wordmark {
    position: absolute;
    left: 0; right: 0;
    text-align: center;
    font-weight: 700;
    font-size: 44px;
    letter-spacing: 0.5px;
    white-space: nowrap;
  }
  .card-back .wordmark { color: var(--silver); top: 170px; }
  .card-front .wordmark { color: var(--ink); top: 60px; }
  .identity {
    position: absolute;
    right: 420px;
    top: 158px;
    text-align: right;
    white-space: nowrap;
  }
  .person-name { font-weight: 700; font-size: 27px; color: var(--ink); }
  .person-role { font-size: 20px; color: var(--brand-red); margin-top: 2px; }
  .divider {
    position: absolute;
    left: 304px; top: 150px;
    width: 1px; height: 138px;
    background: var(--divider);
  }
  .contact {
    position: absolute;
    left: 324px; top: 148px;
    font-size: 19px;
    color: var(--ink);
    line-height: 22px;
    white-space: nowrap;
  }
  .contact-line { display: flex; align-items: center; gap: 8px; }
  .contact-line svg { width: 16px; height: 16px; flex: none; }
  .address { margin-top: 6px; }
  .website {
    position: absolute;
    left: 46px; bottom: 30px;
    color: var(--card-white);
    font-size: 17px;
    letter-spacing: 5px;
  }
</style>
</head>
<body>
  <section class="card card-back">
    <div class="wordmark">Wageline Associates</div>
  </section>

  <section class="card card-front">
    <svg class="card-art" viewBox="0 0 700 400" preserveAspectRatio="none">
      <path d="M0 222 C 150 342, 400 367, 700 362 L700 400 L0 400 Z" fill="var(--brand-red)"/>
      <path d="M0 200 C 150 320, 400 345, 700 340" fill="none" stroke="var(--deep-red)" stroke-width="2"/>
      <path d="M0 212 C 150 332, 400 357, 700 352" fill="none" stroke="var(--brand-red)" stroke-width="1" opacity="0.4"/>
    </svg>

    <div class="wordmark">Wageline Associates</div>

    <div class="identity">
      <div class="person-name">Jonathan Mercer</div>
      <div class="person-role">Managing Director</div>
    </div>

    <div class="divider"></div>

    <div class="contact">
      <div class="contact-line">
        <svg viewBox="0 0 16 16"><path d="M3 1 L6 1 L7 5 L5 6 C6 8.5 7.5 10 10 11 L11 9 L15 10 L15 13 C15 14 14 15 13 15 C6 14 2 10 1 3 C1 2 2 1 3 1 Z" fill="var(--brand-red)"/></svg>
        <span>555-014-2260</span>
      </div>
      <div class="contact-line">
        <svg viewBox="0 0 16 16"><rect x="4" y="1" width="8" height="4" fill="var(--brand-red)"/><rect x="1" y="6" width="14" height="6" rx="1" fill="var(--brand-red)"/><rect x="4" y="10" width="8" height="5" fill="var(--brand-red)" stroke="#fff" stroke-width="1"/></svg>
        <span>555-014-2260</span>
      </div>
      <div class="contact-line">
        <svg viewBox="0 0 16 16"><rect x="1" y="3" width="14" height="10" fill="var(--brand-red)"/><path d="M1 3 L8 9 L15 3" fill="none" stroke="#fff" stroke-width="1.2"/></svg>
        <span>info@wagelineassociates.com</span>
      </div>
      <div class="address">
        180 Harbor Street NW<br>
        Suite 400, Fairview<br>
        MI 49010
      </div>
    </div>

    <div class="website">WWW.WAGELINEASSOCIATES.COM</div>
  </section>
</body>
</html>
```